Brindle Bites - Product Packaging (Snack wrapper)

Brindle Bites is looking for our next package design! Our snack products are all-natural, gluten-free, vegan, and paleo. Our mission is to bring clean, wholesome snacks back into the market. The package design is for our individual wrappers that hold two of our snack bites.

The background will be matte white with a transparent window integrated so that customers can see the bites inside.

The final design will be clean and modern, using white as the background, black for text, and our logos yellow. We have multiple different flavors, so each flavor will have its own unique color accents that must be editable in the final file. The accent colors should be bold and take up an equal amount of space as the white does.

The packaging will stand out on a busy shelf and entice customers as an easy on-the-go, wholesome snack. The back of the package must have a space for a nutrition box and ingredients list. Our logo is attached. The logo graphic can be separated (it doesnt have to stay in the same layout you see). We have attached an example of our old product label, too.

The package dimensions are 4inches wide x 5 inches long with a 1/2inch of the length at the top and 1/2inch of the length at the bottom being blank for sealing. Thank you!

Target Market(s)

Cafe goers, health-conscience, kids, active.

Font styles to use
Sans Serif

Colors
fbed22
ffffff
000000

Requirements
Must have
• Must show that our product is gluten-free, vegan, and paleo. Must have editable flavor name, and flavor accent colors for our multiple different flavors. Must use our logo and company yellow.

```html
<!DOCTYPE html>
<html lang="en">
<head>
<meta charset="utf-8">
<title>Brindle Bites – Chocolate Chip Wrapper Dieline</title>
<link rel="stylesheet" href="https://fonts.googleapis.com/css2?family=Amatic+SC:wght@700&family=Archivo+Black&family=Roboto:wght@400;500;700&family=Roboto+Condensed:wght@300;400;700&display=swap">
<style>
  :root {
    --stage: #121212;
    --wrapper: #cdedfc;
    --brand-yellow: #fbe36e;
    --ink: #1b1b1b;
    --rule: #2a2a2a;
    --dim: #e8e8e8;
    --cookie-light: #b98a63;
    --cookie-dark: #6b4429;
    --inch: 95px;
  }
  * { box-sizing: border-box; margin: 0; padding: 0; }
  html, body { width: 968px; height: 1200px; overflow: hidden; background: var(--stage); }
  body { position: relative; font-family: "Roboto", Arial, sans-serif; color: var(--ink); }

  .panel {
    position: absolute; top: 330px;
    width: calc(var(--inch) * 4); height: calc(var(--inch) * 5);
    background: var(--wrapper);
  }
  .panel--front { left: 40px; }
  .panel--back { left: 508px; }

  .brand-name {
    position: absolute; left: 0; right: 0; text-align: center;
    font-family: "Roboto Condensed", Arial, sans-serif; font-weight: 700;
    color: var(--brand-yellow); line-height: 1;
  }
  .panel--front .brand-name { top: 56px; font-size: 42px; }

  .product-line {
    position: absolute; top: 108px; left: 0; right: 0; text-align: center;
    font-family: "Amatic SC", "Arial Narrow", sans-serif; font-weight: 700;
    font-size: 72px; line-height: 1; letter-spacing: 1px; color: var(--ink);
  }
  .product-photo {
    position: absolute; left: 101px; top: 179px; width: 180px; height: 180px;
    border-radius: 50%;
    background: radial-gradient(circle at 45% 45%, var(--cookie-light), var(--cookie-dark));
  }
  .flavor-name {
    position: absolute; top: 368px; left: 0; right: 0; text-align: center;
    font-family: "Roboto Condensed", Arial, sans-serif; font-weight: 400;
    font-size: 27px; line-height: 1;
  }
  .flavor-rule {
    position: absolute; top: 401px; left: 97px; width: 186px; height: 1px; background: var(--rule);
  }
  .diet-claims {
    position: absolute; top: 404px; left: 0; right: 0; text-align: center;
    font-family: "Roboto", Arial, sans-serif; font-weight: 700;
    font-size: 13.5px; color: var(--brand-yellow); word-spacing: 3px;
  }

  /* Back */
  .nutrition {
    position: absolute; left: 22px; top: 97px; width: 172px;
    border: 1px solid var(--rule); padding: 2px 3px 3px;
    font-size: 7.6px; line-height: 1.2; background: transparent;
  }
  .nutrition__title { font-family: "Archivo Black", Arial, sans-serif; font-size: 17.5px; line-height: 1.05; border-bottom: 1px solid var(--rule); }
  .nutrition__servings { font-size: 8.6px; margin-top: 1px; }
  .nutrition__size { display: flex; justify-content: space-between; font-size: 9.4px; border-bottom: 4px solid var(--rule); padding-bottom: 1px; }
  .nutrition__amount { font-weight: 700; font-size: 7.6px; margin-top: 2px; padding-left: 2px; }
  .nutrition__calories { display: flex; justify-content: space-between; align-items: baseline; padding: 0 0 1px 2px; border-bottom: 3px solid var(--rule); }
  .nutrition__calories span:first-child { font-size: 16px; }
  .nutrition__calories span:last-child { font-family: "Archivo Black", Arial, sans-serif; font-size: 19px; }
  .nutrition__dv { text-align: right; font-weight: 700; font-size: 5.8px; padding: 1px 0; }
  .nutrition__row { display: flex; justify-content: space-between; border-top: 0.8px solid var(--rule); padding: 0.5px 0; }
  .nutrition__row--sub { padding-left: 10px; }
  .nutrition__row--subsub { padding-left: 20px; }
  .nutrition__row--last { border-bottom: 3px solid var(--rule); }
  .nutrition__note { font-size: 5.4px; line-height: 1.25; padding: 2px 0 1px; }
  .nutrition__note + .nutrition__note { border-top: 0.8px solid var(--rule); }

  .ingredients { position: absolute; left: 22px; top: 371px; width: 176px; font-size: 7.5px; line-height: 1.22; }
  .ingredients strong { font-weight: 700; }

  .brand-mark {
    position: absolute; left: 268px; top: 70px; width: 38px; height: 38px;
    border-radius: 50%; background: var(--brand-yellow);
  }
  .panel--back .brand-name { left: 200px; right: 0; top: 113px; font-size: 44px; }
  .pack-title {
    position: absolute; left: 200px; right: 0; top: 173px; text-align: center;
    font-family: "Archivo", "Roboto", Arial, sans-serif; font-weight: 700;
    font-size: 17px; line-height: 1.02;
  }
  .back-rule { position: absolute; left: 218px; width: 135px; height: 1.5px; background: var(--rule); }
  .back-rule--top { top: 216px; }
  .back-rule--bottom { top: 357px; }
  .pack-copy {
    position: absolute; left: 212px; width: 148px; top: 224px; text-align: center;
    font-size: 7.7px; line-height: 1.52;
  }
  .pack-copy p + p { margin-top: 11px; }
  .maker { position: absolute; left: 208px; width: 156px; top: 368px; text-align: center; font-size: 8.2px; line-height: 1.38; }
  .maker .net-weight { margin-top: 3px; }

  /* Dimension callouts */
  .dim-v { position: absolute; top: 330px; height: 475px; width: 1px; background: var(--dim); }
  .dim-v::before, .dim-v::after, .dim-h::before, .dim-h::after {
    content: ""; position: absolute; width: 0; height: 0; border: 3px solid transparent;
  }
  .dim-v::before { top: -3px; left: -3px; border-bottom-color: var(--dim); border-top-width: 0; }
  .dim-v::after { bottom: -3px; left: -3px; border-top-color: var(--dim); border-bottom-width: 0; }
  .dim-h { position: absolute; top: 840px; height: 1px; width: 380px; background: var(--dim); }
  .dim-h::before { left: -3px; top: -3px; border-right-color: var(--dim); border-left-width: 0; }
  .dim-h::after { right: -3px; top: -3px; border-left-color: var(--dim); border-right-width: 0; }
  .seal-tick { position: absolute; width: 17px; height: 1px; background: var(--dim); }
  .dim-label { position: absolute; color: var(--dim); font-size: 10px; font-family: "Roboto", Arial, sans-serif; }
</style>
</head>
<body>

  <section class="panel panel--front" aria-label="Wrapper front">
    <div class="brand-name">Brindle</div>
    <div class="product-line">COOKIE BITES</div>
    <div class="product-photo" role="img" aria-label="Close-up photo of a chocolate chip cookie seen through the window"></div>
    <div class="flavor-name">Chocolate Chip</div>
    <div class="flavor-rule"></div>
    <div class="diet-claims">Gluten-free &bull; Vegan &bull; Paleo</div>
  </section>

  <section class="panel panel--back" aria-label="Wrapper back">
    <div class="nutrition">
      <div class="nutrition__title">Nutrition Facts</div>
      <div class="nutrition__servings">2 Servings Per Container</div>
      <div class="nutrition__size"><span>Serving size</span><span>1 Cookie (29g)</span></div>
      <div class="nutrition__amount">Amount Per Serving</div>
      <div class="nutrition__calories"><span>Calories</span><span>150</span></div>
      <div class="nutrition__dv">% Daily Value*</div>
      <div class="nutrition__row"><span>Total Fat 12g</span><span>15%</span></div>
      <div class="nutrition__row nutrition__row--sub"><span>Saturated Fat 5g</span><span>25%</span></div>
      <div class="nutrition__row nutrition__row--sub"><span>Trans Fat 0g</span><span></span></div>
      <div class="nutrition__row"><span>Sodium 0mg</span><span>0%</span></div>
      <div class="nutrition__row"><span>Total Carbohydrate 9g</span><span>3%</span></div>
      <div class="nutrition__row nutrition__row--sub"><span>Dietary Fiber 2g</span><span>7%</span></div>
      <div class="nutrition__row nutrition__row--sub"><span>Total Sugars 5g</span><span></span></div>
      <div class="nutrition__row nutrition__row--subsub"><span>Includes 5g Added Sugars</span><span>10%</span></div>
      <div class="nutrition__row nutrition__row--last"><span>Protein 4g</span><span>8%</span></div>
      <p class="nutrition__note">Not a significant source of cholesterol, vitamin D, calcium, iron, and potassium</p>
      <p class="nutrition__note">*The % Daily Value (DV) tells you how much a nutrient in a serving of food contributes to a daily diet. 2,000 calories a day is used for general nutrition advice.</p>
    </div>

    <p class="ingredients"><strong>Ingredients:</strong> Almond flour, Organic Maple Syrup, Organic Cold Pressed Coconut Oil, Vegan Chocolate Chips (Cocoa, Cocoa Butter, Sugar), Baking Soda, Sea Salt</p>

    <div class="brand-mark" aria-hidden="true"></div>
    <div class="brand-name">Brindle</div>
    <h1 class="pack-title">Chocolate Chip<br>Cookie Bites</h1>
    <div class="back-rule back-rule--top"></div>
    <div class="pack-copy">
      <p>Soft baked and ready to enjoy anytime the craving hits!</p>
      <p>These delicious cookies are nutritional powerhouses. They are packed with protein and good fats from coconut oil and almonds. Gently sweetened with pure maple syrup, they are sure to satisfy your sweet tooth AND keep you full for hours to come.</p>
    </div>
    <div class="back-rule back-rule--bottom"></div>
    <div class="maker">
      <p>Manufactured by Brindle Bites<br>Fairhaven, CA 90415</p>
      <p class="net-weight">Net Wt. 58 grams</p>
    </div>
  </section>

  <!-- Front dimensions -->
  <div class="dim-v" style="left:468px"></div>
  <div class="seal-tick" style="left:446px; top:370px"></div>
  <div class="seal-tick" style="left:446px; top:765px"></div>
  <span class="dim-label" style="left:446px; top:348px">1/2”</span>
  <span class="dim-label" style="left:446px; top:772px">1/2”</span>
  <span class="dim-label" style="left:478px; top:561px">5”</span>
  <div class="dim-h" style="left:40px"></div>
  <span class="dim-label" style="left:224px; top:850px">4”</span>

  <!-- Back dimensions -->
  <div class="dim-v" style="left:920px"></div>
  <div class="seal-tick" style="left:898px; top:370px"></div>
  <div class="seal-tick" style="left:898px; top:765px"></div>
  <span class="dim-label" style="left:898px; top:348px">1/2”</span>
  <span class="dim-label" style="left:898px; top:772px">1/2”</span>
  <span class="dim-label" style="left:930px; top:561px">5”</span>
  <div class="dim-h" style="left:508px"></div>
  <span class="dim-label" style="left:692px; top:850px">4”</span>

</body>
</html>
```